Flyer for an online formula one racing league

Hello.

I am looking for the perfect one page facebook/instagram style flyer for an online formula one racing league. The racing league is called 'VOLTA RACING LEAGUE'.

Information that MUST be on the new flyer is already on the old flyer I have uploaded here. In addition to including: The Volta racing league 'V' logo I have uploaded AND the text: 'Very popular, clean and competitive racing league, running for its 4th season. Why not join with a friend? Race times, Mondays, Tuesdays and Wednesdays each at 8pm UK TIME Message below for any questions. (Spacing of information is not important, however all the information in regards to the racing I have just mentioned MUST BE on the flyer, this includes info from old pic, logo and the other info I just mentioned).

It would be beneficial to have lots of dark blue on the flyer and the new flyer to be a lot different to the original flyer I uploaded, but this is not essential.

I apologise if I did not explain very well, any questions, please message me.

The best flyer should look the most attractive to someone that might be interested in joining an online formula one racing league.

I used this website before to create the perfect logo for my Sunday League team last year, and I was very impressed. I look forward to seeing your submissions.

Target Market(s)

No specific target, more something that may attract someone into joining a formula one online racing league

Industry/Entity Type

e sports/formula one

Colors
0054AA
0677BA
7BADD7
CADEEF
E8F1F8

Requirements
Must have
• Read product description please
Should not have
• Ignoring product description!

```html
<!DOCTYPE html>
<html lang="en">
<head>
<meta charset="UTF-8">
<title>Volta Racing League – New Season Flyer</title>
<link href="https://fonts.googleapis.com/css2?family=Poppins:ital,wght@0,400;0,600;0,700;0,800;1,400&display=swap" rel="stylesheet">
<style>
  :root {
    --navy: #050b2c;
    --white: #ffffff;
    --pink: #e6007e;
    --blue: #1c1cf0;
    --car-dark: #1a2040;
    --car-mid: #2a2f58;
  }
  * { margin: 0; padding: 0; box-sizing: border-box; }
  html, body {
    width: 1200px;
    height: 849px;
    overflow: hidden;
    background: var(--navy);
  }
  .flyer {
    position: relative;
    width: 1200px;
    height: 849px;
    background: var(--navy);
    font-family: 'Poppins', sans-serif;
    color: var(--white);
    overflow: hidden;
  }
  .flyer > * { position: absolute; }

  .tagline {
    left: 56px;
    top: 48px;
    font-size: 38px;
    font-weight: 700;
    color: var(--pink);
    letter-spacing: -0.3px;
  }
  .league-name {
    left: 52px;
    top: 108px;
    font-size: 126px;
    font-weight: 800;
    line-height: 113px;
    letter-spacing: -1px;
    text-transform: uppercase;
  }
  .schedule {
    left: 57px;
    top: 460px;
    font-size: 25px;
    font-weight: 400;
    line-height: 30px;
  }
  .headline {
    left: 57px;
    top: 576px;
    font-size: 44px;
    font-weight: 700;
    letter-spacing: -0.3px;
    line-height: 1;
  }
  .divisions {
    left: 57px;
    top: 630px;
    font-size: 29px;
    font-weight: 700;
    color: var(--pink);
    letter-spacing: -0.3px;
  }
  .invite {
    left: 600px;
    width: 560px;
    top: 432px;
    text-align: center;
  }
  .invite-season {
    font-size: 39px;
    font-weight: 800;
    line-height: 48px;
    letter-spacing: -0.3px;
  }
  .invite-friend {
    font-size: 33px;
    font-weight: 600;
    line-height: 46px;
  }
  .race-artwork {
    left: 540px;
    top: 110px;
    width: 660px;
    height: 262px;
    background: linear-gradient(90deg, rgba(5,11,44,0) 0%, var(--car-dark) 30%, var(--car-mid) 70%, rgba(5,11,44,0.4) 100%);
    border-radius: 6px;
  }
  .stripe-pink {
    left: 0;
    top: 699px;
    width: 1070px;
    height: 26px;
    background: var(--pink);
  }
  .stripe-blue {
    left: 0;
    top: 734px;
    width: 1070px;
    height: 27px;
    background: var(--blue);
  }
  .brand-mark {
    left: 945px;
    top: 660px;
    width: 130px;
    height: 140px;
    display: flex;
    align-items: center;
    justify-content: center;
    background: var(--navy);
    font-size: 130px;
    font-weight: 800;
    line-height: 1;
    color: var(--white);
  }
  .contact-note {
    left: 58px;
    top: 785px;
    font-size: 23px;
    font-style: italic;
    font-weight: 400;
  }
</style>
</head>
<body>
  <main class="flyer">
    <p class="tagline">Running for its 4th year!</p>

    <h1 class="league-name">Volta<br>Racing<br>League</h1>

    <div class="race-artwork" role="img" aria-label="Illustration of four top-down formula racing cars speeding right, one pink and one blue in front of two dark cars"></div>

    <p class="schedule">Spaces left on Mondays,<br>Tuesdays and Wednesdays<br>each at 8pm UK time</p>

    <div class="invite">
      <p class="invite-season">New season just starting</p>
      <p class="invite-friend">Why not join with a friend?</p>
    </div>

    <h2 class="headline">CLEAN ONLINE RACING LEAGUE</h2>
    <p class="divisions">3 Divisions currently and looking to keep growing!</p>

    <div class="stripe-pink"></div>
    <div class="stripe-blue"></div>

    <div class="brand-mark" aria-label="Volta Racing League">V</div>

    <p class="contact-note">Message below for any questions.</p>
  </main>
</body>
</html>
```